TKA Electricial Contracting Services

Hi guys, after a design for my small electrical company, have logo design files to be incorporated into the layout, the basic concept is electrical contracting services for residential, commercial, industrial & data services, image is clean clear and strong,

Card format is to have a nice clean logo on front,with maybe the Residential – commercial – industrial - data, followed with licensed & insured, followed by contact details on backside of the card.

Target Market(s)

Residential, commercial, industrial sectors.

Industry/Entity Type

Electrical

Contact Information for Business Card

TKA logo,
Residential – commercial – industrial - data
REC: 61372
Email: tka@poralink.net.au
Phone: 0458 203 719

Requirements
Must have
• Clean & strong design.
Nice to have
• If possible, I would like the logo colours inverted so the text is orange and the background is black on the front of the card, then the backside of the card be the reverse colour
Should not have
• No Sparks, lightning bolts,

```html
<!DOCTYPE html>
<html lang="en">
<head>
<meta charset="utf-8">
<title>TKA Electrical – Business Card</title>
<link rel="stylesheet" href="https://fonts.googleapis.com/css2?family=Lato:wght@400;700;900&display=swap">
<style>
  :root {
    --stage: #1d1d1f;
    --ink: #1c1c26;
    --paper: #f4f4f4;
    --paper-shade: #e2e2e2;
    --grey-text: #4a4a4a;
    --white: #ffffff;
  }
  * { box-sizing: border-box; margin: 0; padding: 0; }
  html, body { width: 1200px; height: 873px; overflow: hidden; }
  body {
    background: var(--stage);
    font-family: "Lato", Arial, sans-serif;
    position: relative;
  }
  .card {
    position: absolute;
    width: 520px;
    height: 300px;
    top: 286px;
    overflow: hidden;
    box-shadow: 0 12px 30px rgba(0,0,0,.6);
  }

  /* Front */
  .card-front { left: 50px; background: var(--ink); }
  .front-brand {
    position: absolute; left: 0; right: 0; top: 58px;
    text-align: center; color: var(--white);
  }
  .brand-mark { font-weight: 900; font-size: 74px; line-height: 1; letter-spacing: 2px; }
  .brand-name { font-weight: 900; font-size: 15px; letter-spacing: .5px; margin-top: 2px; }
  .front-band {
    position: absolute; left: 0; right: 0; top: 190px; height: 70px;
    background: linear-gradient(var(--paper), var(--paper-shade));
    display: flex; flex-direction: column; justify-content: center; align-items: center;
    color: var(--grey-text); font-size: 15px; letter-spacing: 1px; gap: 4px;
  }
  .stripe { position: absolute; left: 0; right: 0; height: 4px; background: var(--paper); }
  .card-front .stripe-a { top: 182px; }
  .card-front .stripe-b { top: 268px; }
  .card-front .stripe-c { top: 278px; height: 10px; }

  /* Back */
  .card-back { left: 630px; background: linear-gradient(135deg, var(--white), var(--paper-shade)); }
  .back-brand {
    position: absolute; left: 26px; top: 66px; width: 210px;
    color: var(--ink); text-align: center;
  }
  .back-brand .brand-mark { font-size: 70px; }
  .divider { position: absolute; left: 258px; top: 40px; width: 2px; height: 132px; background: var(--ink); }
  .contact { position: absolute; left: 282px; top: 34px; color: var(--ink); }
  .person-name { font-weight: 700; font-size: 22px; }
  .person-role { font-size: 12px; letter-spacing: 1px; margin: 2px 0 16px 74px; }
  .contact-list { list-style: none; font-size: 13px; line-height: 1.45; }
  .contact-list li { display: flex; align-items: flex-start; gap: 10px; }
  .contact-list svg { flex: none; margin-top: 2px; }
  .back-band {
    position: absolute; left: 0; right: 0; top: 210px; height: 62px;
    background: var(--ink); color: var(--white);
    font-weight: 700; font-size: 13.5px; text-align: center;
    display: flex; flex-direction: column; justify-content: center; gap: 4px;
  }
  .card-back .stripe { background: var(--ink); }
  .card-back .stripe-a { top: 200px; height: 3px; }
  .card-back .stripe-b { top: 280px; height: 3px; }
  .card-back .stripe-c { top: 290px; height: 10px; }
</style>
</head>
<body>
  <section class="card card-front" aria-label="Card front">
    <div class="front-brand">
      <div class="brand-mark">TKA</div>
      <div class="brand-name">Tarkin Alder Electrical</div>
    </div>
    <div class="stripe stripe-a"></div>
    <div class="front-band">
      <p>LICENCED &amp; INSURED</p>
      <p>RESIDENTIAL - COMMERCIAL - INDUSTRIAL</p>
    </div>
    <div class="stripe stripe-b"></div>
    <div class="stripe stripe-c"></div>
  </section>

  <section class="card card-back" aria-label="Card back">
    <div class="back-brand">
      <div class="brand-mark">TKA</div>
      <div class="brand-name">Tarkin Alder Electrical</div>
    </div>
    <div class="divider"></div>
    <div class="contact">
      <p class="person-name">Marco Delgado</p>
      <p class="person-role">INCHARGE</p>
      <ul class="contact-list">
        <li>
          <svg width="14" height="14" viewBox="0 0 14 14" aria-hidden="true"><rect width="14" height="14" rx="3" fill="#1c1c26"/><rect x="4.5" y="2.5" width="5" height="9" rx="1" fill="none" stroke="#fff" stroke-width="1.2"/></svg>
          <span>0458 203 719</span>
        </li>
        <li>
          <svg width="14" height="14" viewBox="0 0 14 14" aria-hidden="true"><rect width="14" height="14" rx="3" fill="#1c1c26"/><rect x="3" y="4" width="8" height="6" fill="#fff"/><path d="M3 4l4 3.2L11 4" fill="none" stroke="#1c1c26" stroke-width="1"/></svg>
          <span>tka@poralink.net.au</span>
        </li>
        <li>
          <svg width="14" height="14" viewBox="0 0 14 14" aria-hidden="true"><rect width="14" height="14" rx="3" fill="#1c1c26"/><path d="M7 2.5a3 3 0 0 1 3 3c0 2.2-3 5.5-3 5.5S4 7.7 4 5.5a3 3 0 0 1 3-3z" fill="#fff"/><circle cx="7" cy="5.5" r="1.1" fill="#1c1c26"/></svg>
          <span>482 Harbour Lane<br>Westfield, Fl 33190</span>
        </li>
      </ul>
    </div>
    <div class="stripe stripe-a"></div>
    <div class="back-band">
      <p>• New installations • Additions • Rewiring • Repairs</p>
      <p>• Maintenance 24 hours • Faults and Emergency Assistance •</p>
    </div>
    <div class="stripe stripe-b"></div>
    <div class="stripe stripe-c"></div>
  </section>
</body>
</html>
```